lighting products eshop web site

We need a brand new ecommerce website (only psd files for the layout) , that will sell professional lighting products in Greek territory.
Please check the sister site www.lampivo.gr to get an idea of the products, they will be similar, actually like the products under the menu category "ΕΠΑΓΓΕΛΜΑΤΙΚΑ".
We would like the same philosophy as far as concern the menu structure, namely the menu categories/subcategories shall be actually the products
categories/subcategories, however the menu items shall be presented in a different, more sophisticated way. As far as concern the website layout, we need a minimal, elegant
and contemporary approach that will highlight the products in a perfect manner. We prefer the white color as the main website (background) color and discrete use of brand logo colors.
That is the main idea, awaiting your personal proposal according to the aforementioned requirements
Technically speaking we use bootstrap framework in terms of design meaning 12cols with max width 1170px.
The website will be a joomla - virtuemart website

For images please use some from lampivo.gr
For text use any text - just to show me the space.

Industry/Entity Type

It Professional

Number of Pages Required

3 page

Font styles to use
Sans Serif

Colors
00a990
ec1f27

Requirements
Must have
• I need 4 psd pages for the website
• 1. Start page
• 2. Category page
• 3. Product details page
• 4. blog page
Nice to have
• leave designer to choose the best

```html
<!DOCTYPE html>
<html lang="el">
<head>
<meta charset="utf-8">
<title>LAMPIVO — Επαγγελματικά προϊόντα φωτισμού</title>
<link rel="stylesheet" href="https://fonts.googleapis.com/css2?family=EB+Garamond:wght@400;500;600;700&display=swap">
<style>
:root{
  --teal:#00a990;
  --teal-soft:#cfe9e5;
  --red:#ec1f27;
  --ink:#222;
  --muted:#777;
  --line:#e4e4e4;
  --gray-bg:#f4f4f4;
  --white:#fff;
}
*{box-sizing:border-box;margin:0;padding:0}
html,body{width:1200px;height:2808px;overflow:hidden;background:var(--white)}
body{font-family:"EB Garamond",Georgia,serif;color:var(--ink);position:relative}

/* header */
.site-header{position:absolute;left:0;top:0;width:1200px;height:108px}
.brand{position:absolute;left:99px;top:32px;font-size:48px;letter-spacing:10px;color:var(--red);font-weight:400;line-height:1}
.search{position:absolute;left:580px;top:45px;width:365px;height:32px;border:1px solid var(--line);font-size:12px;padding:8px 14px;color:#555;letter-spacing:.5px}
.search svg{position:absolute;right:12px;top:9px}
.lang{position:absolute;left:973px;top:54px;font-size:12px;color:#444;letter-spacing:.5px}
.lang span{color:var(--red);font-size:10px}
.cart{position:absolute;left:1078px;top:44px}

.main-nav{position:absolute;left:0;top:108px;width:1200px;height:60px;background:var(--teal);display:flex;align-items:center;padding-left:107px}
.main-nav a{color:var(--white);font-size:13px;letter-spacing:.6px;text-decoration:none;margin-right:27px;white-space:nowrap}
.main-nav a::after{content:" ⌄";font-size:11px}

/* hero */
.hero{position:absolute;left:0;top:168px;width:1200px;height:571px;background:radial-gradient(ellipse at 60% 45%,#3fb24a 0%,#1f8a34 55%,#0f5e24 100%)}
.hero-visual{position:absolute;left:200px;top:20px;width:720px;height:530px;background:radial-gradient(ellipse 38% 50% at 18% 45%,rgba(225,238,232,.75) 0%,rgba(200,222,212,.4) 45%,rgba(0,0,0,0) 100%),linear-gradient(100deg,rgba(0,0,0,0) 30%,rgba(190,215,200,.22) 55%,rgba(0,0,0,0) 95%)}
.hero h1{position:absolute;left:0;top:238px;width:1200px;text-align:center;color:var(--white);font-size:31px;font-weight:700;line-height:1.32;letter-spacing:.4px;text-shadow:0 2px 4px rgba(0,0,0,.35)}
.dots{position:absolute;left:573px;top:514px;display:flex;gap:6px}
.dots i{width:9px;height:9px;border-radius:50%;background:var(--white);display:block}
.dots i.off{background:transparent;border:1.5px solid var(--white)}

/* section title */
.section-title{position:absolute;left:99px;width:1013px;text-align:center;font-size:38px;font-weight:400;letter-spacing:1.5px}
.section-title.lined::before,.section-title.lined::after{content:"";position:absolute;top:50%;width:285px;height:1px;background:var(--line)}
.section-title.lined::before{left:0}
.section-title.lined::after{right:0}
.pager{position:absolute;display:flex;gap:8px}
.pager span{width:24px;height:24px;border:1px solid #cfcfcf;display:flex;align-items:center;justify-content:center;background:var(--white)}

/* cards */
.card{position:absolute;width:238px;background:var(--white);border:1px solid #e8e8e8;box-shadow:0 1px 3px rgba(0,0,0,.06);text-align:center}
.card .thumb{display:block;width:100%;border-bottom:1px solid #eee}
.card .name{font-size:20px;letter-spacing:.5px;margin-top:24px}
.card .price{font-size:25px;font-weight:700;margin-top:4px}
.card .price s{font-weight:400;color:#444;font-size:22px;margin-right:14px}
.card .price.sale{color:var(--red);font-weight:400}
.btn{display:inline-block;background:var(--red);color:var(--white);font-size:13px;letter-spacing:.6px;width:131px;height:37px;line-height:37px}
.badge-new{position:absolute;left:12px;top:16px;background:var(--teal);color:var(--white);font-size:9px;padding:2px 8px;letter-spacing:.5px}

.new-products .card{top:865px;height:427px}
.new-products .thumb{height:258px;margin:0;border:0;border-bottom:1px solid #eee}
.thumb-gold{background:linear-gradient(180deg,#f6f3ee 0%,#ece2cf 55%,#dcc49a 100%)}
.thumb-graphite{background:linear-gradient(180deg,#f5f5f4 0%,#e3e3e1 55%,#c6c6c3 100%)}
.thumb-crimson{background:linear-gradient(180deg,#f6f2f1 0%,#ead9d6 55%,#d7aeaa 100%)}
.thumb-silver{background:linear-gradient(180deg,#f4f5f6 0%,#e2e5e8 55%,#c3c8cd 100%)}
.new-products .btn{margin-top:24px}

.featured{position:absolute;left:0;top:1357px;width:1200px;height:612px;background:var(--gray-bg)}
.tab{position:absolute;top:53px;height:41px;line-height:41px;text-align:center;font-size:19px;letter-spacing:.5px}
.tab.active{left:99px;width:195px;background:var(--teal);color:var(--white)}
.tab.active::after{content:"";position:absolute;left:50%;bottom:-8px;margin-left:-8px;border:8px solid transparent;border-bottom:0;border-top-color:var(--teal)}
.tab.idle{left:309px;width:193px;background:var(--teal-soft);color:#333}
.featured .card{top:131px;height:425px;padding:4px}
.featured .thumb{height:249px;border:0}
.photo-lounge{background:linear-gradient(180deg,#c9a27a 0%,#8c6a4e 30%,#4c3a2d 65%,#2a2420 100%)}
.photo-sofa{background:linear-gradient(180deg,#e4e7e9 0%,#c7cdd2 45%,#a9b0b6 68%,#8e2f33 80%,#5c5d60 100%)}
.photo-dining{background:linear-gradient(180deg,#2f3130 0%,#5f625c 35%,#6f8a4a 62%,#c9b98a 78%,#2e2e2e 100%)}
.photo-garden{background:linear-gradient(180deg,#6a5446 0%,#8a6b4d 30%,#6f7f45 60%,#3f5a2a 100%)}
.featured .name{margin-top:30px}
.featured .btn{margin-top:21px}

/* promo banners */
.promo{position:absolute;top:2016px;width:320px;height:109px;background:var(--white);border:1px solid #ddd;box-shadow:0 1px 4px rgba(0,0,0,.12)}
.promo-inner{position:absolute;left:19px;top:17px;width:282px;height:76px}
.promo-call{background:var(--red);color:var(--white)}
.promo-call .p-brand{position:absolute;left:14px;top:6px;font-size:27px;letter-spacing:4px;line-height:1}
.promo-call .p-phone{position:absolute;left:60px;top:44px;font-size:22px}
.promo-call svg{position:absolute;right:14px;top:22px}
.promo-ship{background:#173f8c;color:var(--white);text-align:center}
.promo-ship .t1{position:absolute;left:0;width:210px;top:14px;font-size:15px}
.promo-ship .t2{position:absolute;left:0;width:210px;top:36px;font-size:9px;line-height:1.25}
.promo-ship .seal{position:absolute;right:10px;top:3px;width:70px;height:70px;border-radius:50%;background:#d22a25;border:3px solid #e9e9e9}
.promo-offer{background:linear-gradient(90deg,#3a3b34 0%,#5c5a4a 45%,#2c2b26 75%,#e6e6e6 75%,#fff 100%)}
.promo-offer .seal{position:absolute;right:6px;top:4px;width:68px;height:68px;border-radius:50%;background:#c72421}

/* manufacturers */
.makers{position:absolute;left:0;top:2181px;width:1200px;height:253px;background:var(--gray-bg)}
.makers .section-title{top:38px}
.maker{position:absolute;top:122px;width:152px;height:71px;background:var(--white);border:1px solid #e3e3e3;display:flex;align-items:center;justify-content:center;font-size:22px;color:#555}
.makers .arrow{position:absolute;top:146px}

/* footer */
.site-footer{position:absolute;left:0;top:2434px;width:1200px;height:374px;background:var(--teal);color:var(--white)}
.site-footer h4{position:absolute;top:47px;font-size:19px;font-weight:400}
.about{position:absolute;left:99px;top:88px;width:225px;font-size:13px;line-height:2.35;color:#e6f6f3}
.links{position:absolute;top:88px;list-style:none;font-size:13px;color:#e6f6f3}
.links li{height:32px;position:relative}
.links li::after{content:"›";position:absolute;left:var(--arrow-x);top:-3px;font-size:17px}
.newsletter-text{position:absolute;left:782px;top:85px;width:330px;font-size:13px;line-height:1.45;color:#e6f6f3}
.signup{position:absolute;left:782px;top:131px;width:330px;height:37px;display:flex}
.signup .field{flex:1;background:var(--white);color:#999;font-size:10px;letter-spacing:1px;padding:12px 16px}
.signup .go{width:107px;background:var(--red);font-size:13px;text-align:center;line-height:37px;letter-spacing:.5px}
.social{position:absolute;left:782px;top:195px;display:flex;gap:10px}
.social i{display:block;width:40px;height:40px;border-radius:50%;background:var(--white)}
.footer-rule{position:absolute;left:99px;top:275px;width:1013px;height:1px;background:rgba(255,255,255,.45)}
.copyright{position:absolute;left:99px;top:305px;font-size:13px;color:#e6f6f3}
</style>
</head>
<body>

<header class="site-header">
  <div class="brand">LAMPIVO</div>
  <div class="search">ΕΡΕΥΝΑ
    <svg width="12" height="12" viewBox="0 0 12 12"><circle cx="5" cy="5" r="3.6" fill="none" stroke="#555" stroke-width="1.4"/><line x1="7.6" y1="7.6" x2="11" y2="11" stroke="#555" stroke-width="1.4"/></svg>
  </div>
  <div class="lang">ΕΛΛΗΝΙΚΑ <span>⌄</span></div>
  <svg class="cart" width="34" height="34" viewBox="0 0 34 34"><path d="M6 12h22l-3 16H9z" fill="none" stroke="#999" stroke-width="1.4"/><path d="M12 12a5 5 0 0 1 10 0" fill="none" stroke="#999" stroke-width="1.4"/><text x="17" y="25" text-anchor="middle" font-size="9" fill="#777" font-family="EB Garamond,serif">0</text></svg>
</header>

<nav class="main-nav">
  <a>ΚΡΕΜΑΣΤΑ</a><a>ΟΡΟΦΗΣ</a><a>ΕΠΙΤΟΙΧΑ</a><a>ΔΑΠΕΔΟΥ</a><a>ΣΠΟΤ</a><a>ΕΞΩΤΕΡΙΚΟΥ ΧΩΡΟΥ</a><a>ΑΝΕΜΙΣΤΗΡΕΣ</a><a>ΕΠΑΓΓΕΛΜΑΤΙΚΑ</a><a>ΕΤΑΙΡΙΕΣ</a>
</nav>

<section class="hero">
  <div class="hero-visual" role="img" aria-label="Σειρά από λάμπες, μία λάμπα LED μπροστά και διάφανες λάμπες πυρακτώσεως πίσω της"></div>
  <h1>ΠΟΥΛΑΜΕ ΕΠΑΓΓΕΛΜΑΤΙΚΑ ΠΡΟΪΟΝΤΑ ΦΩΤΙΣΜΟΥ ΣΤΗΝ<br>ΕΛΛΑΔΑ.</h1>
  <div class="dots"><i></i><i class="off"></i><i></i><i></i></div>
</section>

<section class="new-products">
  <h2 class="section-title lined" style="top:780px">ΝΕΑ ΠΡΟΙΟΝΤΑ</h2>
  <div class="pager" style="left:1054px;top:827px">
    <span><svg width="8" height="10"><path d="M6 1L2 5l4 4" fill="none" stroke="#777" stroke-width="1.3"/></svg></span>
    <span><svg width="8" height="10"><path d="M2 1l4 4-4 4" fill="none" stroke="#777" stroke-width="1.3"/></svg></span>
  </div>
  <article class="card" style="left:99px">
    <div class="thumb thumb-gold" role="img" aria-label="Κρεμαστό φωτιστικό με χρυσό καπέλο"></div>
    <span class="badge-new">ΝΕΟΣ</span>
    <div class="name">ARIANA</div><div class="price">$179.00</div><span class="btn">ΑΓΟΡΑΣΕ ΤΩΡΑ</span>
  </article>
  <article class="card" style="left:357px">
    <div class="thumb thumb-graphite" role="img" aria-label="Κρεμαστό φωτιστικό με γκρι μεταλλικό καπέλο"></div>
    <div class="name">DORIAN</div><div class="price"><s>$120.20</s>$149.00</div><span class="btn">ΑΓΟΡΑΣΕ ΤΩΡΑ</span>
  </article>
  <article class="card" style="left:615px">
    <div class="thumb thumb-crimson" role="img" aria-label="Πολύφωτο κρεμαστό με χρωματιστά καπέλα"></div>
    <div class="name">ELIOS</div><div class="price">$234.00</div><span class="btn">ΑΓΟΡΑΣΕ ΤΩΡΑ</span>
  </article>
  <article class="card" style="left:874px">
    <div class="thumb thumb-silver" role="img" aria-label="Βιομηχανικό κρεμαστό φωτιστικό σε ασημί"></div>
    <div class="name">TERRA</div><div class="price">$228.00</div><span class="btn">ΑΓΟΡΑΣΕ ΤΩΡΑ</span>
  </article>
</section>

<section class="featured">
  <div class="tab active">ΠΡΟΤΕΙΝΟΜΕΝΑ</div>
  <div class="tab idle">ΠΡΟΣΦΟΡΕΣ</div>
  <div class="pager" style="left:1054px;top:56px">
    <span><svg width="8" height="10"><path d="M6 1L2 5l4 4" fill="none" stroke="#777" stroke-width="1.3"/></svg></span>
    <span><svg width="8" height="10"><path d="M2 1l4 4-4 4" fill="none" stroke="#777" stroke-width="1.3"/></svg></span>
  </div>
  <article class="card" style="left:99px">
    <div class="thumb photo-lounge" role="img" aria-label="Μαύρο κρεμαστό φωτιστικό σε σαλόνι αναμονής"></div>
    <div class="name">VOLTA</div><div class="price sale">$342.00</div><span class="btn">ΑΓΟΡΑΣΕ ΤΩΡΑ</span>
  </article>
  <article class="card" style="left:357px">
    <div class="thumb photo-sofa" role="img" aria-label="Ασημί κρεμαστό φωτιστικό πάνω από κόκκινο καναπέ"></div>
    <div class="name">LUNA</div><div class="price sale">$147.00</div><span class="btn">ΑΓΟΡΑΣΕ ΤΩΡΑ</span>
  </article>
  <article class="card" style="left:615px">
    <div class="thumb photo-dining" role="img" aria-label="Λευκό κρεμαστό φωτιστικό πάνω από τραπέζι με φυτά"></div>
    <div class="name">SERENA</div><div class="price sale">$219.00</div><span class="btn">ΑΓΟΡΑΣΕ ΤΩΡΑ</span>
  </article>
  <article class="card" style="left:874px">
    <div class="thumb photo-garden" role="img" aria-label="Πορτοκαλί κρεμαστά φωτιστικά μπροστά σε τοίχο με φυτά"></div>
    <div class="name">CORALLO</div><div class="price sale">$320.00</div><span class="btn">ΑΓΟΡΑΣΕ ΤΩΡΑ</span>
  </article>
</section>

<section class="promos">
  <div class="promo" style="left:99px">
    <div class="promo-inner promo-call">
      <div class="p-brand">LAMPIVO</div>
      <div class="p-phone">801 20000 20</div>
      <svg width="34" height="30" viewBox="0 0 34 30"><path d="M4 12c0-6 26-6 26 0l-3 3-5-2v-3H12v3l-5 2z" fill="#111"/><rect x="9" y="17" width="16" height="11" rx="2" fill="#111"/></svg>
    </div>
  </div>
  <div class="promo" style="left:446px">
    <div class="promo-inner promo-ship">
      <div class="t1">Δωρεάν Αποστολή</div>
      <div class="t2">σε όλη την Ελλάδα για<br>παραγγελίες άνω των<br>200€</div>
      <div class="seal"></div>
    </div>
  </div>
  <div class="promo" style="left:792px">
    <div class="promo-inner promo-offer" role="img" aria-label="Εβδομαδιαίες προσφορές σε φωτιστικά">
      <div class="seal"></div>
    </div>
  </div>
</section>

<section class="makers">
  <h2 class="section-title">ΚΑΤΑΣΚΕΥΑΣΤΕΣ</h2>
  <svg class="arrow" style="left:72px" width="10" height="18"><path d="M8 2L2 9l6 7" fill="none" stroke="#bbb" stroke-width="1.5"/></svg>
  <svg class="arrow" style="left:1129px" width="10" height="18"><path d="M2 2l6 7-6 7" fill="none" stroke="#bbb" stroke-width="1.5"/></svg>
  <div class="maker" style="left:116px">Briolux</div>
  <div class="maker" style="left:281px">Solena</div>
  <div class="maker" style="left:446px">Mirta</div>
  <div class="maker" style="left:611px">Kaldor</div>
  <div class="maker" style="left:776px">Veloria</div>
  <div class="maker" style="left:941px">Ostra</div>
</section>

<footer class="site-footer">
  <h4 style="left:99px">Σχετικά με εμάς</h4>
  <p class="about">Το LAMPIVO σας καλωσορίζει στο φωτεινό ηλεκτρονικό χώρο. Χιλιάδες φωτιστικά που συνεχώς αυξάνονται και ανανεώνονται έχουν επιλεγεί για να φωτίσουν τον χώρο σας στις καλύτερες τιμές.</p>

  <h4 style="left:376px">Υπηρεσίες</h4>
  <ul class="links" style="left:376px;--arrow-x:108px">
    <li>Σύνδεση</li><li>Ιστορικό</li><li>Λίστα Επιθυμιών</li><li>Καλάθι</li><li>Επικοινωνία</li>
  </ul>

  <h4 style="left:558px">Πληροφορίες</h4>
  <ul class="links" style="left:558px;--arrow-x:165px">
    <li>Τρόποι Πληρωμής</li><li>Τρόποι Αποστολής</li><li>Πολιτική Επιστροφών</li><li>Φόρμα Επιστροφών</li>
  </ul>

  <h4 style="left:782px">Εγκύκλιος</h4>
  <p class="newsletter-text">Εγγραφείτε στο newsletter μας για να μαθένετε πρώτοι για τις μοναδικές μας προσφορές!</p>
  <div class="signup"><div class="field">EMAIL ADDRESS</div><div class="go">SUBSCRIBE</div></div>
  <div class="social"><i></i><i></i><i></i><i></i></div>

  <div class="footer-rule"></div>
  <p class="copyright">© 2016 Eponymía Etaireías epifýlaxi pantós dikaiómatos Όroi chrísis</p>
</footer>

</body>
</html>
```